Brivora Collective Business Card Design

We need a business card design for Brivora Collective. We are a healthcare recruiting, wellness and education company. We partner with medical facilities to find quality candidates. We also offer free wellness courses.
The final design should communicate an emphasis on recruiting and wellness
The main purpose of the business card is to utilized it for networking events, give to hospitals, executives, VCs surgery centers and clinics. I want it to be sleek, clean, use of our brand colors and professional.

```html
<!DOCTYPE html>
<html lang="en">
<head>
<meta charset="UTF-8">
<title>Brivora Collective Business Card</title>
<link href="https://fonts.googleapis.com/css2?family=Poppins:wght@300;400;700&display=swap" rel="stylesheet">
<style>
  :root {
    --backdrop: #1e1e1e;
    --card: #0c0c0c;
    --teal: #0b6a62;
    --text-light: #d2d2d2;
    --rule: #4a4a4a;
  }
  html, body {
    margin: 0;
    padding: 0;
    width: 1200px;
    height: 900px;
    overflow: hidden;
    background: var(--backdrop);
    font-family: "Poppins", sans-serif;
  }
  .sheet {
    width: 1200px;
    height: 900px;
    display: flex;
    flex-direction: column;
    align-items: center;
    justify-content: center;
    gap: 40px;
  }
  .card {
    width: 700px;
    height: 400px;
    background: var(--card);
    border-radius: 26px;
    position: relative;
    box-sizing: border-box;
  }
  .card--front {
    display: flex;
    align-items: center;
  }
  .brand-block {
    width: 330px;
    display: flex;
    flex-direction: column;
    align-items: center;
    justify-content: center;
    gap: 14px;
  }
  .brand-square {
    width: 34px;
    height: 34px;
    background: var(--teal);
    border-radius: 6px;
  }
  .brand-name {
    color: var(--teal);
    font-weight: 300;
    font-size: 34px;
    line-height: 1.1;
    text-align: center;
    margin: 0;
  }
  .divider {
    width: 1px;
    height: 230px;
    background: var(--rule);
  }
  .contact-block {
    padding-left: 40px;
    color: var(--text-light);
  }
  .person-name {
    color: var(--teal);
    font-weight: 700;
    font-size: 22px;
    letter-spacing: 0.5px;
    margin: 0;
    text-transform: uppercase;
  }
  .person-role {
    font-weight: 400;
    font-size: 16px;
    margin: 0 0 14px;
  }
  .contact-list {
    list-style: none;
    margin: 0 0 14px;
    padding: 0;
    font-size: 15px;
  }
  .contact-list li {
    display: flex;
    align-items: center;
    gap: 10px;
    line-height: 1.6;
  }
  .contact-icon {
    width: 14px;
    height: 14px;
    flex: none;
  }
  .address {
    font-size: 15px;
    line-height: 1.45;
    margin: 0 0 0 24px;
  }
  .card--back {
    display: flex;
    align-items: center;
    justify-content: center;
    gap: 18px;
  }
  .card--back .brand-square {
    width: 44px;
    height: 44px;
  }
  .card--back .brand-name {
    font-size: 46px;
  }
</style>
</head>
<body>
<main class="sheet">
  <section class="card card--front">
    <div class="brand-block">
      <div class="brand-square"></div>
      <p class="brand-name">Brivora<br>Collective</p>
    </div>
    <div class="divider"></div>
    <div class="contact-block">
      <h1 class="person-name">Marcus Ellery</h1>
      <p class="person-role">Managing Director</p>
      <ul class="contact-list">
        <li>
          <svg class="contact-icon" viewBox="0 0 24 24"><path fill="var(--teal)" d="M6.6 10.8a15 15 0 0 0 6.6 6.6l2.2-2.2c.3-.3.7-.4 1-.2 1.1.4 2.3.6 3.6.6.6 0 1 .4 1 1V20c0 .6-.4 1-1 1A17 17 0 0 1 3 4c0-.6.4-1 1-1h3.5c.6 0 1 .4 1 1 0 1.3.2 2.5.6 3.6.1.3 0 .7-.2 1z"/></svg>
          044-555 018 274
        </li>
        <li>
          <svg class="contact-icon" viewBox="0 0 24 24"><rect x="2" y="5" width="20" height="14" rx="1" fill="var(--teal)"/><path d="M2 6l10 7 10-7" fill="none" stroke="var(--card)" stroke-width="1.8"/></svg>
          hello@brivoracollective.com
        </li>
        <li>
          <svg class="contact-icon" viewBox="0 0 24 24"><g fill="none" stroke="var(--teal)" stroke-width="2"><circle cx="12" cy="12" r="9.5"/><ellipse cx="12" cy="12" rx="4" ry="9.5"/><path d="M2.5 12h19M4 7h16M4 17h16"/></g></svg>
          www.brivoracollective.com
        </li>
      </ul>
      <p class="address">88, Harlow Crescent Suite 4<br>20417, Calderra</p>
    </div>
  </section>
  <section class="card card--back">
    <div class="brand-square"></div>
    <p class="brand-name">Brivora Collective</p>
  </section>
</main>
</body>
</html>
```